Business Card Design Project

we need a business card design for our company: www.plomvik.ch
It's important to include our already existing logo (see website)

```html
<!DOCTYPE html>
<html lang="en">
<head>
<meta charset="utf-8">
<title>Plomvik business card</title>
<link rel="stylesheet" href="https://fonts.googleapis.com/css2?family=Open+Sans:wght@400;600&display=swap">
<style>
  :root {
    --stage: #d9d9d9;
    --card-black: #1a1818;
    --card-white: #ffffff;
    --brand-blue: #3d7bd1;
    --brand-blue-light: #6a9be0;
    --swoosh-blue: #2a6dc6;
    --ink: #1c1c1c;
    --ink-soft: #555555;
    --link-blue: #2f6fc2;
    --on-dark: #f2f2f2;
  }
  * { box-sizing: border-box; margin: 0; padding: 0; }
  html, body { width: 1200px; height: 951px; overflow: hidden; }
  body {
    background: var(--stage);
    font-family: "Open Sans", Arial, sans-serif;
    position: relative;
  }
  .card {
    position: absolute;
    width: 620px;
    height: 380px;
    border-radius: 22px;
    overflow: hidden;
    box-shadow: 0 6px 18px rgba(0,0,0,0.25);
  }
  .card--back {
    left: 90px;
    top: 70px;
    background: var(--card-black);
    display: flex;
    align-items: center;
    justify-content: center;
  }
  .card--back .brand-name {
    font-size: 128px;
    font-weight: 600;
    color: var(--brand-blue-light);
    letter-spacing: -2px;
  }
  .card--front {
    left: 490px;
    top: 500px;
    background: var(--card-white);
  }
  .front-shapes { position: absolute; inset: 0; }
  .front-brand {
    position: absolute;
    left: 38px;
    top: 22px;
    font-size: 64px;
    font-weight: 600;
    color: var(--brand-blue);
    letter-spacing: -1px;
    line-height: 1;
  }
  .address {
    position: absolute;
    left: 40px;
    top: 128px;
    font-size: 17px;
    line-height: 22px;
    color: var(--ink);
  }
  .contact-list {
    position: absolute;
    left: 40px;
    top: 212px;
    list-style: none;
    font-size: 17px;
    line-height: 26px;
    color: var(--ink);
  }
  .contact-list li { display: flex; align-items: center; gap: 10px; }
  .contact-list svg { width: 13px; height: 13px; flex: none; }
  .contact-list .web { color: var(--link-blue); }
  .holder {
    position: absolute;
    right: 34px;
    bottom: 30px;
    text-align: right;
    color: var(--on-dark);
  }
  .holder-name { font-size: 22px; line-height: 28px; }
  .holder-role { font-size: 16px; line-height: 22px; }
</style>
</head>
<body>

  <section class="card card--back" aria-label="Business card, back">
    <span class="brand-name">Plomvik</span>
  </section>

  <section class="card card--front" aria-label="Business card, front">
    <svg class="front-shapes" viewBox="0 0 620 380" aria-hidden="true">
      <path d="M408 0 Q395 230 228 380 L262 380 Q425 220 438 0 Z" fill="var(--swoosh-blue)"/>
      <path d="M438 0 L620 0 L620 380 L262 380 Q425 220 438 0 Z" fill="var(--card-black)"/>
    </svg>

    <div class="front-brand">Plomvik</div>

    <address class="address" style="font-style:normal">
      Plomvik AG<br>
      Lindenhofweg 12<br>
      8045 Zürich
    </address>

    <ul class="contact-list">
      <li>
        <svg viewBox="0 0 16 16"><path d="M4 1 L6.5 4.5 L5 6.5 Q6.5 9.5 9.5 11 L11.5 9.5 L15 12 L13 15 Q6 14 1 3 Z" fill="var(--ink)"/></svg>
        +41 44 310 47 80
      </li>
      <li>
        <svg viewBox="0 0 16 16"><rect x="1" y="3" width="14" height="10" rx="1" fill="none" stroke="var(--ink)" stroke-width="1.6"/><path d="M1.5 3.5 L8 9 L14.5 3.5" fill="none" stroke="var(--ink)" stroke-width="1.6"/></svg>
        info@plomvik.ch
      </li>
      <li>
        <svg viewBox="0 0 16 16"><circle cx="8" cy="8" r="6.5" fill="none" stroke="var(--ink)" stroke-width="1.6"/><circle cx="8" cy="8" r="2" fill="var(--ink)"/></svg>
        plomvik.ch
      </li>
      <li class="web">
        <svg viewBox="0 0 16 16"><rect x="1.5" y="2" width="13" height="9" fill="none" stroke="var(--ink)" stroke-width="1.6"/><path d="M4 14 H12" stroke="var(--ink)" stroke-width="1.6"/></svg>
        www.plomvik.ch
      </li>
    </ul>

    <div class="holder">
      <div class="holder-name">Lena Marthaler</div>
      <div class="holder-role">Manager</div>
    </div>
  </section>

</body>
</html>
```